KPL Business Card Design

I am attaching my logo and want both a black and white modern, contemporary card for my business.

Below are the details I require on the cards and of course I would need to be able to change this.

Thanks

Rob

Robert J Harcourt

Sales & Marketing Director

 

Vivid Panel Gazette

PO Box 4417

Chatham

Kent

ME7 5QX

 

Tel +44 (0) 1632 960 418

Mobile: +44 (0) 7700 900 537

Fax: +44 (0) 1632 960 772

Email: rob@vividpanelgazette.example

Website: www.vividpanelgazette.example

 

 

Be part of a World full of imagination,

knowledge and inspiration

 

 

Derek Pashley

Editorial Director

 

Vivid Panel Gazette

42 Fernhurst Close

Ashcombe

Westvale

TW7 4LN

 

Tel: +44 (0) 208 496 0213

Mobile: +44 (0) 7700 900 864

Email: derek@vividpanelgazette.example

 

 

knowledge and inspiration

This is the same font as used in the logo.......

Robert J Harcourt

 

Vivid Panel Gazette

PO Box 4417

Chatham

Kent

ME7 5QX

 

Tel +44 (0) 1632 960 418

Fax: +44 (0) 1632 960 772

 

 

Derek Pashley

Editorial Director

 

Vivid Panel Gazette

42 Fernhurst Close

Ashcombe

Westvale

TW7 4LN

 

Tel: +44 (0) 208 496 0213

Please add the following words to the back of the card and maybe add the logo to the back again.....

knowledge and inspiration

Robert J Harcourt

 

Vivid Panel Gazette

PO Box 4417

Chatham

Kent

ME7 5QX

 

Tel +44 (0) 1632 960 418

Fax: +44 (0) 1632 960 772

 

 

Derek Pashley

Editorial Director

 

Vivid Panel Gazette

42 Fernhurst Close

Ashcombe

Westvale

TW7 4LN

 

Tel: +44 (0) 208 496 0213

knowledge and inspiration

Target Market(s)

Wide Format printing, Screen Printing, Digital Printing, Textile Printing, Signage, Digital Signage, Exhibition Graphics, Digital Textiles and more

Industry/Entity Type

Publishing

Requirements
Must have
• I would like to use these words on the back of the card both for a full black card and white card.

"Be part of a World full of imagination, knowledge and inspiration"

```html
<!DOCTYPE html>
<html lang="en">
<head>
<meta charset="utf-8">
<title>Vivid Panel Gazette – Business Cards</title>
<link href="https://fonts.googleapis.com/css2?family=Open+Sans:wght@400;600&display=swap" rel="stylesheet">
<style>
  :root {
    --ink: #000;
    --paper: #fff;
    --orange: #f08a24;
    --blue: #1ea7e1;
    --grey: #7a7a7a;
    --bar-dark: #6e6e6e;
    --bar-light: #c8c8c8;
  }
  html, body {
    margin: 0;
    padding: 0;
    width: 1116px;
    height: 1200px;
    overflow: hidden;
    background: var(--paper);
    font-family: "Open Sans", sans-serif;
  }
  .sheet { position: relative; width: 1116px; height: 1200px; }

  .card {
    position: absolute;
    width: 282px;
    height: 551px;
    overflow: hidden;
    box-shadow: 6px 6px 9px rgba(0, 0, 0, 0.35);
  }
  .card--black { background: var(--ink); color: var(--paper); }
  .card--white { background: var(--paper); color: var(--ink); }
  .card--front.card--black { left: 50px; top: 0; }
  .card--front.card--white { left: 800px; top: 0; }
  .card--back.card--black  { left: 50px; top: 612px; }
  .card--back.card--white  { left: 800px; top: 612px; }

  /* landscape layer read bottom-to-top */
  .turned {
    position: absolute;
    left: 0;
    top: 551px;
    width: 551px;
    height: 282px;
    transform-origin: 0 0;
    transform: rotate(-90deg);
  }
  .divider {
    position: absolute;
    left: 308px;
    top: 136px;
    width: 218px;
    height: 11px;
    background: linear-gradient(to bottom, var(--bar-dark), var(--bar-light));
  }

  /* front */
  .identity, .contact {
    position: absolute;
    left: 308px;
    margin: 0;
    white-space: nowrap;
  }
  .identity { top: 60px; line-height: 19px; }
  .identity__name { font-size: 18px; display: block; line-height: 22px; }
  .identity__role, .identity__email { font-size: 13px; display: block; }
  .contact { top: 157px; font-size: 13px; line-height: 19px; font-style: normal; }
  .contact__gap { display: block; height: 4px; }
  .contact__label { color: var(--orange); }
  .card--white .identity__role,
  .card--white .identity__email,
  .card--white .contact__address { color: var(--grey); }
  .card--white .contact__label { color: var(--ink); }

  .brand {
    position: absolute;
    left: 22px;
    top: 362px;
    display: flex;
    align-items: center;
    gap: 12px;
  }
  .brand__mark {
    width: 64px;
    height: 64px;
    border-radius: 50%;
    background: var(--blue);
  }
  .brand__name {
    font-size: 24px;
    font-weight: 600;
    line-height: 26px;
    color: var(--orange);
  }

  /* back */
  .motto {
    position: absolute;
    left: 310px;
    margin: 0;
    font-size: 17px;
    line-height: 21.5px;
    letter-spacing: 2px;
    color: var(--orange);
    white-space: nowrap;
  }
  .motto--lead { top: 38px; }
  .motto--tail { top: 153px; }

  .web {
    position: absolute;
    left: 20px;
    top: 402px;
    width: 236px;
    line-height: 1;
  }
  .web__prefix { display: block; font-size: 15px; color: var(--grey); letter-spacing: 1px; }
  .web__domain { display: block; font-size: 22px; margin-left: 14px; letter-spacing: 0.2px; }
  .web__domain .a { color: var(--orange); }
  .web__domain .c { color: var(--blue); }
  .web__suffix { display: block; text-align: right; font-size: 15px; color: var(--grey); }
</style>
</head>
<body>
<main class="sheet">

  <!-- front, black -->
  <section class="card card--front card--black">
    <div class="turned">
      <p class="identity">
        <span class="identity__name">Derek Pashley</span>
        <span class="identity__role">Managing Editor</span>
        <span class="identity__email">derek@vividpanelgazette.example</span>
      </p>
      <div class="divider"></div>
      <address class="contact">
        <span class="contact__address">42 Fernhurst Close, Ashcombe,<br>Westvale, TW7 4LN</span>
        <span class="contact__gap"></span>
        <span class="contact__label">T</span> : +44 (0) 208 496 0213<br>
        <span class="contact__label">M</span> : +44 (0) 7700 900 864
      </address>
    </div>
    <div class="brand">
      <span class="brand__mark"></span>
      <span class="brand__name">Vivid Panel<br>Gazette</span>
    </div>
  </section>

  <!-- front, white -->
  <section class="card card--front card--white">
    <div class="turned">
      <p class="identity">
        <span class="identity__name">Derek Pashley</span>
        <span class="identity__role">Managing Editor</span>
        <span class="identity__email">derek@vividpanelgazette.example</span>
      </p>
      <div class="divider"></div>
      <address class="contact">
        <span class="contact__address">42 Fernhurst Close, Ashcombe,<br>Westvale, TW7 4LN</span>
        <span class="contact__gap"></span>
        <span class="contact__label">T</span> : +44 (0) 208 496 0213<br>
        <span class="contact__label">M</span> : +44 (0) 7700 900 864
      </address>
    </div>
    <div class="brand">
      <span class="brand__mark"></span>
      <span class="brand__name">Vivid Panel<br>Gazette</span>
    </div>
  </section>

  <!-- back, black -->
  <section class="card card--back card--black">
    <div class="turned">
      <p class="motto motto--lead">Be<br>part of<br>a World<br>full of</p>
      <div class="divider"></div>
      <p class="motto motto--tail">imagination<br>knowledge<br>and<br>inspiration</p>
    </div>
    <p class="web">
      <span class="web__prefix">www.</span>
      <span class="web__domain"><span class="a">vivid</span><span class="b">panel</span><span class="c">gazette</span></span>
      <span class="web__suffix">.example</span>
    </p>
  </section>

  <!-- back, white -->
  <section class="card card--back card--white">
    <div class="turned">
      <p class="motto motto--lead">Be<br>part of<br>a World<br>full of</p>
      <div class="divider"></div>
      <p class="motto motto--tail">imagination<br>knowledge<br>and<br>inspiration</p>
    </div>
    <p class="web">
      <span class="web__prefix">www.</span>
      <span class="web__domain"><span class="a">vivid</span><span class="b">panel</span><span class="c">gazette</span></span>
      <span class="web__suffix">.example</span>
    </p>
  </section>

</main>
</body>
</html>
```